Lip Balm Label Design

Design a label for a Lavender-Mint lip balm. We make high-quality natural essential oil products. Please use the old label as an example of what exists. The label should include purple. The final design should be eye-catching and distinct. The file should be in an AI file.

Here is the information that should be included on the label:
1) ingredients:Theobroma Cacao (Cocoa) Seed Butter, Theobroma grandiflorum Ultra Refined Butter, beesewax, Calendula Officinalis Flower Oil, Prunus Amygdalus Dulcis (Sweet Almond) Oil, cetyl alcohol and Tocopherol. Lavandula Angustifolia (Lavender) Oil and Mentha Piperita (Peppermint) Oil.

2) www.kelvorascents.com

3) Brand name and logo: K. Velora Aromatherapy (logo is attached- you can use with form)

```html
<!DOCTYPE html>
<html lang="en">
<head>
<meta charset="utf-8">
<title>Lavender Mint Lip Balm Label</title>
<link rel="stylesheet" href="https://fonts.googleapis.com/css2?family=Cormorant+Garamond:wght@300&family=Josefin+Sans:wght@300;400&family=Allura&display=swap">
<style>
  :root {
    --backdrop: #6b4f93;
    --lavender: #b8b4d9;
    --lavender-deep: #aca7d0;
    --white: #ffffff;
    --ink-muted: #5d5a86;
  }
  * { margin: 0; padding: 0; box-sizing: border-box; }
  html, body { width: 1200px; height: 1200px; overflow: hidden; }
  body { background: var(--backdrop); position: relative; }

  .label {
    position: absolute; left: 211px; top: 105px;
    width: 778px; height: 990px;
    background: var(--white);
    overflow: hidden;
  }
  .label__front {
    position: absolute; left: 0; top: 0;
    width: 570px; height: 990px;
    background: var(--lavender);
    overflow: hidden;
  }
  .label__motif {
    position: absolute; left: 40px; top: 180px;
    width: 340px; height: 780px;
    background: radial-gradient(ellipse at 55% 50%, var(--lavender-deep) 0%, rgba(184,180,217,0) 70%);
  }

  .brand {
    position: absolute; left: 108px; top: 68px;
    display: flex; align-items: center; gap: 14px;
    color: var(--white);
    font-family: "Cormorant Garamond", serif; font-weight: 300;
    font-size: 30px; letter-spacing: 1px; white-space: nowrap;
  }
  .brand__dot { width: 34px; height: 34px; border-radius: 50%; background: var(--white); opacity: .85; }

  .vertical {
    position: absolute;
    writing-mode: vertical-rl;
    transform: rotate(180deg);
    white-space: nowrap;
    color: var(--white);
  }
  .product-name {
    left: 92px; top: 198px; height: 556px;
    font-family: "Cormorant Garamond", serif; font-weight: 300;
    font-size: 104px; line-height: 1; letter-spacing: 6px;
  }
  .product-flavor {
    left: 178px; top: 466px;
    font-family: "Allura", cursive;
    font-size: 172px; line-height: 1;
  }
  .product-type {
    position: absolute; left: 108px; top: 808px;
    color: var(--white);
    font-family: "Josefin Sans", sans-serif; font-weight: 400;
    font-size: 50px; letter-spacing: 9px; white-space: nowrap;
  }
  .product-size {
    position: absolute; left: 108px; top: 890px;
    color: var(--white);
    font-family: "Josefin Sans", sans-serif; font-weight: 300;
    font-size: 24px; white-space: nowrap;
  }
  .website {
    left: 494px; top: 726px; height: 186px;
    font-family: "Josefin Sans", sans-serif; font-weight: 400;
    font-size: 9px; letter-spacing: 2.4px; text-transform: uppercase;
  }

  .ingredients {
    position: absolute; left: 655px; top: 84px;
    height: 818px; width: 72px;
    writing-mode: vertical-rl;
    transform: rotate(180deg);
    color: var(--ink-muted);
    font-family: "Josefin Sans", sans-serif; font-weight: 400;
    font-size: 13.6px; line-height: 17px;
    text-transform: uppercase; text-align: justify;
  }
</style>
</head>
<body>
  <div class="label">
    <div class="label__front">
      <div class="label__motif" role="img" aria-label="Soft lavender leaf motif behind the product name"></div>

      <div class="brand"><span class="brand__dot"></span>K. Velora Aromatherapy</div>

      <div class="vertical product-name">LAVENDER</div>
      <div class="vertical product-flavor">mint</div>

      <div class="product-type">LIP BALM</div>
      <div class="product-size">0.15 OZ (4.4 ML)</div>

      <div class="vertical website">www.kelvorascents.com</div>
    </div>

    <p class="ingredients">Ingredients: Theobroma Cacao (Cocoa) Seed Butter, Theobroma Grandiflorum Ultra Refined Butter, Beesewax, Calendula Officinalis Flower Oil, Prunus Amygdalus Dulcis (Sweet Almond) Oil, Cetyl Alcohol and Tocopherol. Lavandula Angustifolia (Lavender) Oil and Mentha Piperita (Peppermint) Oil.</p>
  </div>
</body>
</html>
```